Business Card for Lorena Whitfield

Name: Lorena Whitfield
Title: Realtor
Email: Lorena@LorenaWhitfieldRE.com
Phone: 480-555-0137

On the front of the business card, I would like the photo, the contact information and the Lorena Whitfield Logo. The backside is required to have the Broker logo and the required logos. Please use the colors from the logo design. Our company has a classy, professional look.

```html
<!DOCTYPE html>
<html lang="en">
<head>
<meta charset="UTF-8">
<title>Lorena Whitfield – Business Card</title>
<link href="https://fonts.googleapis.com/css2?family=Cinzel:wght@400;500&family=Arimo:wght@400&display=swap" rel="stylesheet">
<style>
  :root {
    --page: #2b2b2b;
    --card: #0c0c0c;
    --red: #c8102e;
    --white: #f2f2f2;
    --grey: #9a9a9a;
    --rule-front: #e6e6e6;
    --rule-back: #5a5a5a;
    --photo-light: #8e8e8e;
    --photo-dark: #1a1a1a;
  }
  * { margin: 0; padding: 0; box-sizing: border-box; }
  html, body { width: 1200px; height: 900px; overflow: hidden; background: var(--page); }
  .canvas {
    width: 1200px; height: 900px;
    display: flex; flex-direction: column; align-items: center; justify-content: center; gap: 50px;
  }
  .card {
    position: relative; width: 630px; height: 360px;
    background: var(--card); overflow: hidden;
    box-shadow: 0 12px 30px rgba(0,0,0,.5);
  }
  .card::after {
    content: ""; position: absolute; left: 0; right: 0; bottom: 0; height: 10px; background: var(--red);
  }
  .serif { font-family: "Cinzel", serif; }
  .sans { font-family: "Arimo", Arial, sans-serif; }

  /* brand lockup */
  .brand { position: absolute; display: flex; align-items: center; gap: 12px; }
  .brand-mark { width: 38px; height: 38px; border: 2px solid var(--red); flex: none; }
  .brand-text { display: flex; flex-direction: column; }
  .brand-name { color: var(--red); font-size: 20px; letter-spacing: 1px; line-height: 1; white-space: nowrap; }
  .brand-sub { display: flex; align-items: center; gap: 6px; margin-top: 3px; }
  .brand-rule { flex: 1; height: 1px; background: var(--rule-front); }
  .brand-tag { color: var(--white); font-size: 9px; letter-spacing: 1px; white-space: nowrap; }

  /* front */
  .portrait {
    position: absolute; left: 0; top: 0; bottom: 10px; width: 290px;
    background: radial-gradient(ellipse at 45% 45%, var(--photo-light) 0%, #555 40%, var(--photo-dark) 80%);
  }
  .front .brand { left: 312px; top: 46px; }
  .divider {
    position: absolute; left: 300px; top: 140px; width: 1px; height: 170px; background: #3a3a3a;
  }
  .agent { position: absolute; left: 320px; top: 150px; }
  .agent-name { color: var(--red); font-size: 22px; font-weight: 400; letter-spacing: 1px; line-height: 1; white-space: nowrap; }
  .agent-title { color: var(--white); font-size: 14px; letter-spacing: 1px; margin-top: 6px; }
  .contact { list-style: none; margin-top: 18px; }
  .contact li { display: flex; align-items: center; gap: 10px; color: var(--white); font-size: 15px; margin-bottom: 8px; white-space: nowrap; }
  .contact svg { width: 15px; height: 15px; flex: none; }

  /* back */
  .back .brand { left: 70px; top: 110px; }
  .back .brand-mark { width: 46px; height: 46px; }
  .back .brand-name { font-size: 26px; }
  .back .brand-rule { background: var(--rule-back); }
  .back .brand-tag { color: var(--grey); font-size: 11px; }
  .broker {
    position: absolute; right: 50px; top: 190px; display: flex; align-items: center; gap: 10px;
  }
  .broker-mark { width: 30px; height: 30px; border-radius: 50%; border: 1.5px solid var(--grey); }
  .broker-name { color: var(--grey); font-size: 14px; letter-spacing: 1px; }
  .badges { position: absolute; left: 235px; top: 260px; display: flex; gap: 10px; align-items: center; }
  .badge { border: 2px solid var(--white); }
  .badge.house { width: 34px; height: 34px; }
  .badge.member { width: 34px; height: 34px; }
  .badge.listing { width: 62px; height: 28px; background: var(--white); }
</style>
</head>
<body>
<main class="canvas">
  <section class="card front">
    <div class="portrait" role="img" aria-label="Black and white portrait photo of the realtor"></div>
    <div class="brand">
      <span class="brand-mark"></span>
      <div class="brand-text serif">
        <span class="brand-name">Lorena Whitfield</span>
        <div class="brand-sub"><span class="brand-rule"></span><span class="brand-tag">REAL ESTATE</span></div>
      </div>
    </div>
    <div class="divider"></div>
    <div class="agent">
      <h1 class="agent-name serif">LORENA WHITFIELD</h1>
      <p class="agent-title sans">REALTOR</p>
      <ul class="contact sans">
        <li>
          <svg viewBox="0 0 24 24"><path fill="var(--red)" d="M6.6 10.8a15 15 0 0 0 6.6 6.6l2.2-2.2a1 1 0 0 1 1-.25 11.4 11.4 0 0 0 3.6.57 1 1 0 0 1 1 1V20a1 1 0 0 1-1 1A17 17 0 0 1 3 4a1 1 0 0 1 1-1h3.5a1 1 0 0 1 1 1c0 1.25.2 2.45.57 3.57a1 1 0 0 1-.25 1z"/></svg>
          480-555-0137
        </li>
        <li>
          <svg viewBox="0 0 24 24"><path fill="var(--red)" d="M2 5h20v14H2z M2 5l10 8 10-8" stroke="var(--card)" stroke-width="1.5"/></svg>
          Lorena@LorenaWhitfieldRE.com
        </li>
        <li>
          <svg viewBox="0 0 24 24" fill="none" stroke="var(--red)" stroke-width="2"><circle cx="12" cy="12" r="9"/><path d="M3 12h18M12 3c3 3 3 15 0 18M12 3c-3 3-3 15 0 18"/></svg>
          www.LorenaWhitfieldRE.com
        </li>
      </ul>
    </div>
  </section>

  <section class="card back">
    <div class="brand">
      <span class="brand-mark"></span>
      <div class="brand-text serif">
        <span class="brand-name">Lorena Whitfield</span>
        <div class="brand-sub"><span class="brand-rule"></span><span class="brand-tag">REAL ESTATE</span></div>
      </div>
    </div>
    <div class="broker">
      <span class="broker-mark"></span>
      <span class="broker-name serif">Harlow Crest Realty</span>
    </div>
    <div class="badges">
      <span class="badge house"></span>
      <span class="badge member"></span>
      <span class="badge listing"></span>
    </div>
  </section>
</main>
</body>
</html>
```